Tallowick Limited Business Card

We need a business card for a new company based in Essex, United Kingdom. We develop and manufacture educational games. The business card needs to match the company brand and logo and the colour scheme.
My company makes educational board games to be played by the family or used by teachers
The games are tile based number game

Target Market(s)

Parents, teachers, schools and children

Industry/Entity Type

Games

Contact Information for Business Card

Company Name - Tallowick Limited
Director - Damian Prouse
Registered Office - 3 Marsh Court, 142 Quarry Lane, Brindleford, Essex, CM7 4XR
Phone Number - 07950 000 318
Email - Enquiries@Tallowick.example
Website - www.Tallowick.example
Company Number - 00000000

Font styles to use
Sans Serif

Colors
00a990
ffffff

Requirements
Must have
• Same colour scheme as the attachments - green and white
• Same font style for Tallowick
• Images of the number tiles similar to the attachments
• extra details
• The colour is Cyan - 82 Magenta - 24 Yellow - 44 Black - 2
• I have attached some of the font styles use on my website and alos my LOGO
Nice to have
• Image of the number "1" tag as seen on the website

```html
<!DOCTYPE html>
<html lang="en">
<head>
<meta charset="utf-8">
<title>Tallowick Limited Business Card</title>
<link href="https://fonts.googleapis.com/css2?family=Open+Sans:wght@300;400;600;800&display=swap" rel="stylesheet">
<style>
  :root {
    --teal: #1b9a99;
    --teal-deep: #15898a;
    --white: #ffffff;
    --stage: #2f3133;
  }
  * { margin: 0; padding: 0; box-sizing: border-box; }
  html, body {
    width: 1200px; height: 896px; overflow: hidden;
    background: var(--stage);
    font-family: "Open Sans", Arial, sans-serif;
  }
  .card {
    position: absolute;
    left: 325px;
    width: 550px; height: 316px;
    border-radius: 24px;
    overflow: hidden;
    background: linear-gradient(135deg, var(--teal) 0%, var(--teal-deep) 100%);
    color: var(--white);
    box-shadow: 0 10px 28px rgba(0,0,0,.45);
  }
  .card--front { top: 104px; }
  .card--back  { top: 476px; }

  /* front */
  .front-brand {
    position: absolute; left: 150px; top: 92px;
  }
  .brand-name {
    font-weight: 800; font-size: 60px; line-height: 1; letter-spacing: -1px;
    position: relative; display: inline-block;
  }
  .brand-mark {
    position: absolute; right: -14px; top: 4px;
    width: 9px; height: 9px; border-radius: 50%;
    border: 1.5px solid currentColor;
  }
  .brand-tagline {
    font-size: 19px; font-weight: 400; letter-spacing: .2px; margin-top: 6px;
  }
  .company-number {
    font-size: 19px; font-weight: 400; margin-top: 4px;
  }

  /* back */
  .back-band {
    position: absolute; left: 0; top: 0; bottom: 0; width: 136px;
    background: var(--white);
  }
  .band-brand {
    position: absolute; left: 68px; top: 158px;
    width: 300px;
    transform: translate(-50%, -50%) rotate(-90deg);
    color: var(--teal);
    text-align: center;
  }
  .band-brand .brand-name { font-size: 54px; }
  .band-brand .brand-tagline { font-size: 17px; margin-top: 4px; }

  .contact {
    position: absolute; right: 34px; top: 40px;
    text-align: right;
  }
  .contact-name {
    font-size: 30px; font-weight: 600; letter-spacing: .5px; line-height: 1.1;
  }
  .contact-role { font-size: 14px; font-weight: 400; margin-bottom: 16px; }
  .contact-line {
    font-size: 15px; line-height: 25px;
    display: flex; justify-content: flex-end; align-items: center; gap: 8px;
  }
  .contact-line svg { width: 12px; height: 12px; flex: none; }
  .contact-address { font-size: 15px; line-height: 22px; margin-top: 4px; padding-right: 20px; }
</style>
</head>
<body>

<section class="card card--front" aria-label="Card front">
  <div class="front-brand">
    <div class="brand-name">Tallowick<span class="brand-mark"></span></div>
    <div class="brand-tagline">FAST PACED NUMBER GAMES</div>
    <div class="company-number">Company Number - 00000000</div>
  </div>
</section>

<section class="card card--back" aria-label="Card back">
  <div class="back-band">
    <div class="band-brand">
      <div class="brand-name">Tallowick<span class="brand-mark"></span></div>
      <div class="brand-tagline">FAST PACED NUMBER GAMES</div>
    </div>
  </div>

  <div class="contact">
    <div class="contact-name">DAMIAN PROUSE</div>
    <div class="contact-role">Director</div>
    <div class="contact-line">07950 000 318
      <svg viewBox="0 0 12 12" aria-hidden="true"><path d="M3 1l2 2.5-1.2 1.3a6 6 0 0 0 3.4 3.4L8.5 7 11 9l-1.3 2A9 9 0 0 1 1 2.3z" fill="#fff"/></svg>
    </div>
    <div class="contact-line">Enquiries@Tallowick.example
      <svg viewBox="0 0 12 12" aria-hidden="true"><rect x="1" y="2.5" width="10" height="7" rx="1" fill="none" stroke="#fff" stroke-width="1.2"/><path d="M1.5 3l4.5 3.5L10.5 3" fill="none" stroke="#fff" stroke-width="1.2"/></svg>
    </div>
    <div class="contact-line">www.Tallowick.example
      <svg viewBox="0 0 12 12" aria-hidden="true"><circle cx="6" cy="6" r="5" fill="none" stroke="#fff" stroke-width="1.1"/><ellipse cx="6" cy="6" rx="2.2" ry="5" fill="none" stroke="#fff" stroke-width="1"/><path d="M1 6h10" stroke="#fff" stroke-width="1"/></svg>
    </div>
    <div class="contact-address">3 Marsh Court, 142 Quarry Lane,<br>Brindleford, Essex, CM7 4XR</div>
  </div>
</section>

</body>
</html>
```